Tidewren Calculator Redesign

Tidewren is jewelry featuring the picture of the moon from the date of your choice such as your birthday or anniversarry. People come to our moon phase calculator page (you are designing) to see what the moon looked like on a specific date. I have attached a draft for inspiration. We would like the mockup in both mobile and desktop please.

Give us your best designs to have people engaged with our moon phase calculator page and want to continue navigating and shopping the site
Updates

The Moon must be black so it seems realistic.

Target Market(s)

Woman and men, 25-45

Industry/Entity Type

Jewelry

Colors
6B429C
8869AF
B7A5CE
E3DAEB
F3F0F8

Requirements
Must have
• The moon phase date selection and content speaking about their moonphase
Should not have
• Pink

```html
<!DOCTYPE html>
<html lang="en">
<head>
<meta charset="utf-8">
<title>Tidewren — Moon Phase Calculator Presentation</title>
<link href="https://fonts.googleapis.com/css2?family=Jost:wght@300;400;500;600&display=swap" rel="stylesheet">
<style>
:root{
  --board:#e3e4f1;
  --indigo:#52478b;
  --lilac:#b8bce2;
  --blush:#ece7ed;
  --violet:#6b429c;
  --lavender:#b7a5ce;
  --mist:#f3f0f8;
  --ink:#2d2a45;
  --muted:#8b87a3;
  --night:#1c1d33;
  --white:#ffffff;
}
*{box-sizing:border-box;margin:0;padding:0}
html,body{width:1200px;height:3482px;overflow:hidden}
body{background:var(--board);font-family:"Jost",sans-serif;color:var(--ink);position:relative}
.abs{position:absolute}
.brand-mark{display:flex;align-items:center;gap:8px;color:var(--indigo);font-weight:400;letter-spacing:.18em;white-space:nowrap}
.brand-mark .dot{width:9px;height:9px;border-radius:50%;background:var(--indigo)}
.divider-v{position:absolute;width:1px;background:#c9c9dd}
.board-title{font-size:21px;color:var(--indigo);font-weight:400}
.board-text{font-size:17px;color:#6d6a9a;line-height:1.35}
.swatch{position:absolute;width:36px;height:36px;border-radius:50%}
.swatch-label{position:absolute;font-size:8px;color:#6d6a9a}
.side-label{position:absolute;font-size:18px;letter-spacing:.5em;color:var(--indigo);transform:rotate(-90deg);transform-origin:left top;white-space:nowrap}

.page{position:absolute;background:var(--white);overflow:hidden}
.topbar{position:absolute;left:0;right:0;background:var(--lilac);color:var(--indigo);display:flex;justify-content:space-between;align-items:center;white-space:nowrap}
.nav{position:absolute;left:0;right:0;background:var(--white);display:flex;align-items:center}
.nav-links{display:flex;color:var(--ink);white-space:nowrap}
.hero{position:absolute;left:0;right:0;background:radial-gradient(circle at 75% 40%,#2d3050 0%,#1c1d33 55%,#121325 100%);color:var(--white)}
.moon{position:absolute;border-radius:50%;background:radial-gradient(circle at 30% 35%,#dcdcde 0%,#a4a4aa 30%,#6a6a72 55%,#2e2e36 80%,#16161d 100%)}
.eyebrow{letter-spacing:.35em;text-transform:uppercase;color:#d6d6e6;white-space:nowrap}
.hero-title{font-weight:600;line-height:1.25}
.pill{position:absolute;border:1px solid #8d8fb6;border-radius:20px;display:flex;align-items:center;color:var(--white);white-space:nowrap}
.pill .btn{margin-left:auto;background:var(--lilac);color:var(--indigo);border-radius:20px;font-weight:500;display:flex;align-items:center;justify-content:center}
.u-link{text-decoration:underline;color:#e6e6f2;white-space:nowrap}
.photo{position:absolute;overflow:hidden}
.ph-white{background:radial-gradient(ellipse at 45% 65%,#ffffff 0%,#eceaf2 40%,#d3cde3 80%,#c3b9da 100%)}
.ph-dark{background:linear-gradient(155deg,#d4cbe8 0%,#f1f0f4 35%,#9a9aa4 60%,#2a2a32 85%,#3c3c46 100%)}
.ph-gold{background:radial-gradient(ellipse at 60% 55%,#ffffff 0%,#eeebf0 45%,#d9d2e4 75%,#bdb2d6 100%)}
.ph-people{background:linear-gradient(180deg,#cbc6ea 0%,#b3acdc 50%,#948dc6 100%)}
.ph-blog{background:radial-gradient(ellipse at 50% 60%,#d9d4ec 0%,#c6bfe2 60%,#b4acd8 100%)}
.ph-hand{background:linear-gradient(120deg,#d8c8c4 0%,#eee7ea 45%,#c9c0d6 75%,#a99fc6 100%)}
.ph-neck{background:radial-gradient(ellipse at 40% 70%,#d8dcef 0%,#eeeef4 35%,#f6f5f9 100%)}
.ph-product{background:radial-gradient(ellipse at 45% 70%,#dcdff0 0%,#ece8ef 45%,#e4dee8 100%)}
.ph-thumb{background:linear-gradient(180deg,#e9e8f0 0%,#c9c4dc 40%,#8b7f86 60%,#2b2b36 100%)}
.blog-word{position:absolute;left:0;right:0;text-align:center;color:#fff;font-weight:600;letter-spacing:.08em;line-height:1}
.card-title{color:var(--ink)}
.card-text{color:var(--muted);line-height:1.5}
.card-link{color:var(--indigo);text-decoration:underline}
.section-title{position:absolute;left:0;right:0;text-align:center;color:var(--ink)}
.section-sub{position:absolute;left:0;right:0;text-align:center;color:var(--muted)}
.btn-solid{background:var(--indigo);color:var(--white);display:flex;align-items:center;justify-content:center}
.btn-outline{border:1px solid var(--indigo);color:var(--indigo);display:flex;align-items:center;justify-content:center;text-align:center}
.press-badge{position:absolute;background:#d6d3e6;border-radius:3px}
.footer{position:absolute;left:0;right:0;background:var(--mist)}
.foot-head{position:absolute;color:var(--indigo);letter-spacing:.1em;font-weight:500}
.foot-list{position:absolute;list-style:none;color:var(--muted);white-space:nowrap}
.social{display:flex;gap:6px}
.social span{border:1px solid var(--indigo);border-radius:50%}
</style>
</head>
<body>

<!-- Board header -->
<div class="abs" style="left:270px;top:122px;width:190px;height:70px">
  <svg class="abs" style="left:80px;top:0" width="30" height="30" viewBox="0 0 30 30"><circle cx="15" cy="15" r="4" fill="#52478b"/></svg>
  <div class="abs brand-mark" style="left:10px;top:36px;font-size:24px">TIDEWREN</div>
</div>
<div class="divider-v" style="left:511px;top:122px;height:82px"></div>
<div class="abs board-title" style="left:571px;top:120px">Fonts:</div>
<div class="abs board-text" style="left:571px;top:162px">Lumen Sans<br>Font Family</div>
<div class="divider-v" style="left:725px;top:122px;height:82px"></div>
<div class="abs board-title" style="left:784px;top:120px">Colors:</div>
<div class="swatch" style="left:786px;top:152px;background:var(--indigo)"></div>
<div class="swatch" style="left:833px;top:152px;background:var(--lilac)"></div>
<div class="swatch" style="left:880px;top:152px;background:var(--blush)"></div>
<div class="swatch-label" style="left:786px;top:197px">#52478b</div>
<div class="swatch-label" style="left:833px;top:197px">#b8bce2</div>
<div class="swatch-label" style="left:880px;top:197px">#ece7ed</div>

<!-- Flat hero screen -->
<section class="page" style="left:351px;top:308px;width:585px;height:327px">
  <div class="topbar" style="top:0;height:13px;font-size:5px;padding:0 30px"><span>5% of All Full Moon Purchases Goes to Help The Tide Trust · SHOP NOW</span><span>Free Shipping on All Orders Over $50 · SHOP BEST SELLERS</span></div>
  <div class="nav" style="top:13px;height:46px;padding:0 34px">
    <div class="brand-mark" style="font-size:13px"><span class="dot" style="width:6px;height:6px"></span>TIDEWREN</div>
    <div class="nav-links" style="margin-left:150px;gap:34px;font-size:6px"><span>SHOP</span><span>GIFTS</span><span>HOLIDAY SALE</span><span>OUR STORY</span></div>
  </div>
  <div class="hero" style="top:59px;height:268px">
    <div class="moon" role="img" aria-label="Photograph of the moon" style="left:312px;top:18px;width:210px;height:210px"></div>
    <div class="abs eyebrow" style="left:78px;top:86px;font-size:6px">Ready to discover your moon phase?</div>
    <div class="abs hero-title" style="left:78px;top:98px;font-size:17px">Tidewren's Interactive<br>Moon Phase Calculator</div>
    <div class="abs" style="left:78px;top:150px;font-size:7px;color:#d6d6e6;line-height:1.6">Discover your moon phase or learn more about the moon<br>here using our movable moon or date calculator</div>
    <div class="pill" style="left:78px;top:180px;width:196px;height:22px;font-size:6px;padding:0 3px 0 12px;gap:22px"><span>01 ⌄</span><span>FEB ⌄</span><span>2021 ⌄</span><span class="btn" style="width:48px;height:16px">CALCULATE</span></div>
  </div>
</section>

<div class="side-label" style="left:118px;top:2300px">LAPTOP / DESKTOP</div>
<div class="side-label" style="left:936px;top:2176px">MOBILE</div>

<!-- Desktop page -->
<main class="page" style="left:158px;top:859px;width:588px;height:2498px">
  <div class="topbar" style="top:0;height:16px;font-size:5px;padding:0 38px"><span>5% of All Full Moon Purchases Goes to Help The Tide Trust · <u>SHOP NOW</u></span><span>Free Shipping on All Orders Over $50 · <u>SHOP BEST SELLERS</u></span></div>
  <div class="nav" style="top:16px;height:54px;padding:0 36px">
    <div class="brand-mark" style="font-size:13px"><span class="dot" style="width:6px;height:6px"></span>TIDEWREN</div>
    <div class="nav-links" style="margin-left:120px;gap:30px;font-size:6px"><span>SHOP</span><span>GIFTS</span><span>HOLIDAY SALE</span><span>OUR STORY</span></div>
    <svg style="margin-left:auto" width="36" height="10" viewBox="0 0 36 10"><circle cx="4" cy="3" r="2" fill="#52478b"/><rect x="1" y="6" width="6" height="4" rx="2" fill="#52478b"/><rect x="14" y="2" width="6" height="7" fill="#52478b"/><circle cx="29" cy="4" r="3" fill="none" stroke="#52478b" stroke-width="1.2"/><line x1="31" y1="6" x2="34" y2="9" stroke="#52478b" stroke-width="1.2"/></svg>
  </div>
  <section class="hero" style="top:70px;height:365px">
    <div class="moon" role="img" aria-label="Photograph of the moon" style="left:329px;top:10px;width:256px;height:256px"></div>
    <div class="abs eyebrow" style="left:80px;top:75px;font-size:6px">Ready to discover your moon phase?</div>
    <div class="abs hero-title" style="left:80px;top:92px;font-size:18px">Tidewren's Interactive<br>Moon Phase Calculator</div>
    <div class="abs" style="left:80px;top:141px;font-size:7px;color:#d6d6e6;line-height:1.7">Discover your moon phase or learn more about the moon<br>here using our movable moon or date calculator</div>
    <div class="pill" style="left:80px;top:179px;width:208px;height:24px;font-size:6px;padding:0 3px 0 12px;gap:24px"><span>01 ⌄</span><span>FEB ⌄</span><span>2021 ⌄</span><span class="btn" style="width:52px;height:18px">CALCULATE</span></div>
    <div class="abs u-link" style="left:80px;top:223px;font-size:5px">LEARN MORE ABOUT THE WANING CRESCENT</div>
    <div class="abs" style="left:0;right:0;top:300px;height:65px;background:rgba(20,20,40,.55);border-top:1px solid #3a3c5a">
      <div class="divider-v" style="left:197px;top:0;height:65px;background:#3a3c5a"></div>
      <div class="divider-v" style="left:392px;top:0;height:65px;background:#3a3c5a"></div>
      <svg class="abs" style="left:80px;top:22px" width="20" height="20"><circle cx="10" cy="10" r="9" fill="#b8bce2"/><circle cx="14" cy="10" r="8" fill="#1c1d33"/></svg>
      <div class="abs" style="left:107px;top:22px;font-size:8px;white-space:nowrap">Lunar Pair<br><span style="font-size:5px;color:#b9b9cc">waning gibbous</span></div>
      <svg class="abs" style="left:236px;top:22px" width="20" height="20"><circle cx="10" cy="10" r="8" fill="none" stroke="#b8bce2" stroke-width="1.5"/><circle cx="10" cy="10" r="3" fill="#b8bce2"/></svg>
      <div class="abs" style="left:263px;top:22px;font-size:8px;white-space:nowrap">Lunar Personality<br><span style="font-size:5px;color:#b9b9cc">trait one, trait two, trait three</span></div>
      <svg class="abs" style="left:430px;top:22px" width="24" height="20"><path d="M2 4h8M6 4v14M12 8c4 0 8 2 8 5s-3 5-6 5" fill="none" stroke="#b8bce2" stroke-width="1.5"/></svg>
      <div class="abs" style="left:460px;top:22px;font-size:8px;white-space:nowrap">Moon Sign<br><span style="font-size:5px;color:#b9b9cc">capricorn</span></div>
    </div>
  </section>

  <!-- feature cards -->
  <div class="photo ph-white" role="img" aria-label="Birth moon pendant necklaces on a white stand" style="left:38px;top:473px;width:165px;height:132px"></div>
  <div class="photo ph-dark" role="img" aria-label="Silver tie clip with moon image" style="left:212px;top:473px;width:165px;height:132px"></div>
  <div class="photo ph-gold" role="img" aria-label="Gold moon bangle on a white block" style="left:386px;top:473px;width:165px;height:132px"></div>
  <div class="abs" style="left:38px;top:618px;width:165px;font-size:8px"><div class="card-title">Your Birth Moon</div><div class="card-text" style="font-size:5px;margin-top:6px">The Waning Gibbous as a birth moon means that you are trait one, trait two, trait three.</div><div class="card-link" style="font-size:5px;margin-top:5px">LEARN MORE</div></div>
  <div class="abs" style="left:212px;top:618px;width:165px;font-size:8px"><div class="card-title">Your Anniversary</div><div class="card-text" style="font-size:5px;margin-top:6px">The Waning Gibbous is an auspicious moon to begin relationships or mark milestones under...</div><div class="card-link" style="font-size:5px;margin-top:5px">LEARN MORE</div></div>
  <div class="abs" style="left:386px;top:618px;width:165px;font-size:8px"><div class="card-title">Your Moon Sign</div><div class="card-text" style="font-size:5px;margin-top:6px">This phase combined with your moon sign creates a personality that is uniquely you...</div><div class="card-link" style="font-size:5px;margin-top:5px">LEARN MORE</div></div>
  <div class="abs" style="left:38px;top:704px;width:513px;height:1px;background:#e6e4ee"></div>

  <!-- product detail -->
  <div class="section-title" style="top:741px;font-size:13px">Keep Your Phase Close to Heart</div>
  <div class="section-sub" style="top:766px;font-size:5px">Lorem ipsum dolor amet ningun posteam tidewren necklaces</div>
  <div class="photo ph-neck" role="img" aria-label="Necklace photo thumbnail" style="left:78px;top:800px;width:29px;height:28px"></div>
  <div class="photo ph-neck" role="img" aria-label="Necklace photo thumbnail" style="left:78px;top:831px;width:29px;height:28px"></div>
  <div class="photo ph-neck" role="img" aria-label="Necklace photo thumbnail" style="left:78px;top:862px;width:29px;height:28px;outline:1px solid #b8bce2"></div>
  <div class="photo ph-hand" role="img" aria-label="Model wearing the necklace" style="left:78px;top:893px;width:29px;height:28px"></div>
  <div class="photo ph-hand" role="img" aria-label="Model wearing the necklace" style="left:78px;top:924px;width:29px;height:28px"></div>
  <div class="photo ph-thumb" role="img" aria-label="Necklace in gift box" style="left:78px;top:955px;width:29px;height:28px"></div>
  <div class="photo" role="img" aria-label="Necklace glowing in the dark" style="left:78px;top:986px;width:29px;height:25px;background:linear-gradient(135deg,#1f2330,#3b4a4c)"></div>
  <div class="photo ph-neck" role="img" aria-label="Silver necklace with blue moon pendant" style="left:112px;top:800px;width:192px;height:211px"></div>
  <div class="abs" style="left:335px;top:804px;width:174px">
    <div style="font-size:9px;color:var(--indigo)">Quiet Orbit Necklace</div>
    <div style="font-size:8px;color:var(--indigo);font-weight:500;margin-top:7px">$49.00</div>
    <div class="card-text" style="font-size:5px;margin-top:5px">Pay in full or in 4 interest-free installments for orders between $50 and $3000 with Paylane</div>
    <div style="margin-top:12px;border:1px solid #e0deea;height:20px;font-size:5px;display:flex;align-items:center;gap:6px;padding:0 4px"><span style="width:12px;height:12px;background:#1c1d33;border-radius:2px"></span>13 / FEB / 2022</div>
    <div style="margin-top:8px;font-size:5px;color:var(--muted)">☐ Add Engraving</div>
    <div style="margin-top:5px;border:1px solid #e0deea;height:14px;font-size:5px;color:var(--muted);display:flex;align-items:center;padding:0 5px">Type Your Message Here (Optional)</div>
    <div class="card-text" style="font-size:4px;margin-top:5px">*Engraving is charged as an additional cost<br><u style="color:var(--indigo)">VIEW ENGRAVING PRICING HERE</u></div>
    <div class="btn-solid" style="margin-top:12px;height:24px;font-size:5px">ADD TO CART</div>
  </div>

  <!-- product row -->
  <div class="photo ph-product" role="img" aria-label="Silver necklace with moon pendant" style="left:38px;top:1086px;width:121px;height:122px"></div>
  <div class="photo ph-product" role="img" aria-label="Gold chain necklace with blue pendant" style="left:168px;top:1086px;width:121px;height:122px"></div>
  <div class="abs" style="left:262px;top:1090px;width:22px;height:8px;background:var(--lilac);color:#fff;font-size:4px;text-align:center;line-height:8px">SALE</div>
  <div class="photo ph-product" role="img" aria-label="White beaded bracelet with moon charm" style="left:299px;top:1086px;width:121px;height:122px"></div>
  <div class="photo ph-product" role="img" aria-label="Gold necklace with pendant" style="left:430px;top:1086px;width:121px;height:122px"></div>
  <div class="abs" style="left:38px;top:1222px;width:121px;text-align:center;font-size:6px">Dawnline Necklace in Silver<br><span style="color:var(--lavender)">$49</span></div>
  <div class="abs" style="left:168px;top:1222px;width:121px;text-align:center;font-size:6px">Meridian Necklace in Gold<br><span style="color:var(--lavender)"><s>$66</s> $60</span></div>
  <div class="abs" style="left:299px;top:1222px;width:121px;text-align:center;font-size:6px">Bright Tide Bracelet in White<br><span style="color:var(--lavender)">Sold Out</span></div>
  <div class="abs" style="left:430px;top:1222px;width:121px;text-align:center;font-size:6px">Harbor Necklace in Gold<br><span style="color:var(--lavender)">$95</span></div>

  <!-- moments -->
  <div class="photo ph-people" role="img" aria-label="Customers sitting on a sofa sharing their moments" style="left:80px;top:1277px;width:428px;height:282px">
    <div class="abs" style="left:0;right:0;top:46px;text-align:center;color:#fff;font-size:12px">Moments that Matter</div>
    <div class="abs" style="left:0;right:0;top:70px;text-align:center;color:#eeeaf7;font-size:5px">Read some of our favorite moments that we have had the privilege of being able to help immortalize</div>
    <div class="abs" style="left:0;right:0;top:130px;text-align:center;color:var(--indigo);font-size:8px">Tidewren Moment #128,005</div>
    <div class="abs" style="left:110px;right:110px;top:148px;text-align:center;color:var(--indigo);font-size:5px;line-height:1.7">Lorem ipsum dolor sit amet, consectetur adipiscing elit, sed doe eiusmod tempor incididunt ut labore et dolore magna aliqua. Quis ipsum suspendisse ultrices gravida. Risus commodo viverra ma.</div>
    <svg class="abs" style="left:202px;top:218px" width="24" height="4"><circle cx="2" cy="2" r="1.5" fill="#fff"/><circle cx="12" cy="2" r="1.5" fill="#52478b"/><circle cx="22" cy="2" r="1.5" fill="#fff"/></svg>
  </div>

  <div class="abs" style="left:38px;top:1597px;width:513px;height:114px;background:var(--mist)">
    <div class="abs" style="left:40px;top:38px;font-size:4px;letter-spacing:.1em;color:var(--muted)">CELEBRATING YOUR LIFE</div>
    <div class="abs" style="left:40px;top:50px;font-size:12px;line-height:1.1">Moments<br>that Matter</div>
    <div class="abs card-text" style="left:150px;top:36px;width:215px;font-size:5px;line-height:1.9">Whether for yourself or as a gift to your nearest and dearest, Tidewren helps people stay connected to the memories that have shaped their life. We believe that having a permanent moment of the Moments that shape us helps stay connected to our true selves in the good and the hard times.</div>
    <div class="abs btn-outline" style="left:399px;top:45px;width:72px;height:24px;font-size:4px">WHAT MOMENT WILL<br>YOU REMEMBER?</div>
  </div>

  <!-- blog -->
  <div class="section-title" style="top:1747px;font-size:13px">Learn More About The Phases Now</div>
  <div class="section-sub" style="top:1771px;font-size:5px">Recent Blog Posts</div>
  <div class="photo ph-blog" role="img" aria-label="Capricorn essentials artwork with script lettering" style="left:80px;top:1801px;width:136px;height:133px"><div class="blog-word" style="top:40px;font-size:12px">CAPRICORN</div></div>
  <div class="photo ph-blog" role="img" aria-label="Libra essentials artwork with script lettering" style="left:227px;top:1801px;width:136px;height:133px"><div class="blog-word" style="top:38px;font-size:12px">THE LIBRA</div></div>
  <div class="photo ph-blog" role="img" aria-label="Sagittarius essentials artwork with script lettering" style="left:373px;top:1801px;width:136px;height:133px"><div class="blog-word" style="top:34px;font-size:11px">THE<br>SAGITTARIUS</div></div>
  <div class="abs" style="left:80px;top:1947px;width:136px;font-size:7px"><div>The Capricorn Essentials</div><div class="card-text" style="font-size:5px;margin-top:5px">You set goals, both large and small and always striving to succeed. Your accomplishments are...</div><div class="card-link" style="font-size:4px;margin-top:4px">READ MORE</div></div>
  <div class="abs" style="left:227px;top:1947px;width:136px;font-size:7px"><div>The Libra Essentials:</div><div class="card-text" style="font-size:5px;margin-top:5px">You set goals, both large and small and always striving to succeed. Your accomplishments are...</div><div class="card-link" style="font-size:4px;margin-top:4px">READ MORE</div></div>
  <div class="abs" style="left:373px;top:1947px;width:136px;font-size:7px"><div>The Saggitarius Essentials</div><div class="card-text" style="font-size:5px;margin-top:5px">You set goals, both large and small and always striving to succeed. Your accomplishments are...</div><div class="card-link" style="font-size:4px;margin-top:4px">READ MORE</div></div>

  <!-- signup -->
  <div class="abs" style="left:38px;top:2034px;width:255px;height:148px;background:var(--indigo);color:#fff">
    <div class="abs" style="left:0;right:0;top:48px;text-align:center;font-size:10px">Sign up for 10% off your first purchase*</div>
    <div class="abs" style="left:0;right:0;top:63px;text-align:center;font-size:4px;color:#cfcbe8">*Some exclusions apply</div>
    <div class="abs" style="left:30px;top:80px;width:198px;height:22px;background:#fff;display:flex"><span style="flex:1;font-size:4px;color:var(--muted);padding:8px 6px">Enter your email address here*</span><span style="width:62px;background:var(--lilac);font-size:4px;text-align:center;line-height:22px">SIGN UP NOW</span></div>
  </div>
  <div class="abs" style="left:293px;top:2034px;width:258px;height:148px;background:var(--lilac)">
    <div class="abs" style="left:0;right:0;top:48px;text-align:center;font-size:10px;color:#fff">Gifts for various occasions</div>
    <div class="abs" style="left:0;right:0;top:63px;text-align:center;font-size:4px;color:#fff">Some exclusions apply</div>
    <div class="abs btn-solid" style="left:97px;top:80px;width:64px;height:22px;font-size:4px">SHOP GIFTS</div>
  </div>
  <div class="press-badge" style="left:80px;top:2222px;width:56px;height:12px"></div>
  <div class="press-badge" style="left:205px;top:2222px;width:80px;height:12px"></div>
  <div class="press-badge" style="left:355px;top:2222px;width:56px;height:12px"></div>
  <div class="press-badge" style="left:480px;top:2222px;width:28px;height:12px"></div>

  <footer class="footer" style="top:2270px;height:228px">
    <div class="foot-head" style="left:38px;top:43px;font-size:6px">HELP</div>
    <ul class="foot-list" style="left:38px;top:62px;font-size:5px;line-height:2.6"><li>FAQs</li><li>Contact Us</li><li>Rewards</li><li>Track Your Order</li><li>Reviews</li><li>My Account</li></ul>
    <div class="foot-head" style="left:196px;top:43px;font-size:6px">COMPANY</div>
    <ul class="foot-list" style="left:196px;top:62px;font-size:5px;line-height:2.6"><li>About Us</li><li>Blog</li><li>Careers</li><li>Tours</li><li>Wholesale</li><li>Partnerships</li></ul>
    <div class="foot-head" style="left:357px;top:43px;font-size:6px">SHOP</div>
    <ul class="foot-list" style="left:357px;top:62px;font-size:5px;line-height:2.6"><li>Find Your Moon</li><li>Necklaces</li><li>Bracelets</li><li>Rings</li><li>Gifts</li><li>Deals</li></ul>
    <div class="foot-head" style="left:512px;top:43px;font-size:6px">FIND US</div>
    <div class="abs social" style="left:512px;top:62px"><span style="width:6px;height:6px"></span><span style="width:6px;height:6px"></span><span style="width:6px;height:6px"></span><span style="width:6px;height:6px"></span></div>
    <div class="abs" style="left:30px;top:181px;font-size:5px;color:var(--muted)">Copyright © Tidewren, LLC. All rights reserved.</div>
    <div class="abs" style="left:466px;top:181px;font-size:5px;color:var(--muted)">Terms &amp; Conditions | Privacy Policy</div>
  </footer>
</main>

<!-- Mobile page -->
<main class="page" style="left:975px;top:859px;width:96px;height:2498px">
  <div class="topbar" style="top:0;height:7px;font-size:2px;padding:0 4px"><span>Free Shipping on All Orders Over $50</span><span>SHOP</span></div>
  <div class="nav" style="top:7px;height:24px;justify-content:center"><div class="brand-mark" style="font-size:4px;gap:3px"><span class="dot" style="width:3px;height:3px"></span>TIDEWREN</div></div>
  <section class="hero" style="top:31px;height:170px">
    <div class="moon" role="img" aria-label="Photograph of the moon" style="left:18px;top:10px;width:60px;height:60px"></div>
    <div class="abs eyebrow" style="left:0;right:0;top:88px;text-align:center;font-size:2.5px;letter-spacing:.15em">Ready to discover your moon phase?</div>
    <div class="abs hero-title" style="left:0;right:0;top:95px;text-align:center;font-size:6px">Tidewren's Interactive<br>Moon Phase Calculator</div>
    <div class="pill" style="left:6px;top:118px;width:84px;height:11px;font-size:2.5px;padding:0 1px 0 5px;gap:6px"><span>01 ⌄</span><span>FEB ⌄</span><span>2021 ⌄</span><span class="btn" style="width:22px;height:8px">CALCULATE</span></div>
    <div class="abs u-link" style="left:0;right:0;top:136px;text-align:center;font-size:2.5px">LEARN MORE ABOUT THE WANING CRESCENT</div>
  </section>
  <div class="photo ph-white" role="img" aria-label="Birth moon pendant necklaces" style="left:7px;top:219px;width:84px;height:64px"></div>
  <div class="abs" style="left:7px;top:288px;width:84px;font-size:3.5px"><div>Your Birth Moon</div><div class="card-text" style="font-size:2.5px">The Waning Gibbous as a birth moon means you are trait one, trait two.</div><div class="card-link" style="font-size:2.5px">LEARN MORE</div></div>
  <div class="photo ph-dark" role="img" aria-label="Silver tie clip with moon image" style="left:7px;top:323px;width:84px;height:62px"></div>
  <div class="abs" style="left:7px;top:390px;width:84px;font-size:3.5px"><div>Your Anniversary</div><div class="card-text" style="font-size:2.5px">An auspicious moon to begin relationships or mark milestones.</div><div class="card-link" style="font-size:2.5px">LEARN MORE</div></div>
  <div class="photo ph-gold" role="img" aria-label="Gold moon bangle" style="left:7px;top:427px;width:84px;height:65px"></div>
  <div class="abs" style="left:7px;top:497px;width:84px;font-size:3.5px"><div>Your Moon Sign</div><div class="card-text" style="font-size:2.5px">This phase with your moon sign creates a unique personality.</div><div class="card-link" style="font-size:2.5px">LEARN MORE</div></div>
  <div class="photo ph-hand" role="img" aria-label="Hand wearing a moon bracelet" style="left:0;top:546px;width:96px;height:78px"></div>
  <div class="abs" style="left:7px;top:630px;width:84px;font-size:3.5px"><div>Lunar Tide Bracelets</div><div class="card-text" style="font-size:2.5px">Lorem ipsum dolor sit amet ningun posteam bracelets for every phase.</div><div class="card-link" style="font-size:2.5px">SHOP NOW</div></div>
  <div class="abs" style="left:7px;top:680px;font-size:4px">Keep Your Phase Close<br>to Heart</div>
  <div class="photo ph-neck" role="img" aria-label="Necklace photo thumbnail" style="left:7px;top:719px;width:10px;height:18px"></div>
  <div class="photo ph-hand" role="img" aria-label="Model wearing the necklace" style="left:7px;top:739px;width:10px;height:18px"></div>
  <div class="photo ph-hand" role="img" aria-label="Model wearing the necklace" style="left:7px;top:759px;width:10px;height:18px"></div>
  <div class="photo ph-thumb" role="img" aria-label="Necklace in gift box" style="left:7px;top:779px;width:10px;height:18px"></div>
  <div class="photo ph-neck" role="img" aria-label="Silver necklace with blue moon pendant" style="left:20px;top:719px;width:71px;height:78px"></div>
  <div class="abs" style="left:7px;top:805px;width:84px">
    <div style="font-size:3.5px;color:var(--indigo)">Quiet Orbit Necklace</div>
    <div style="font-size:3.5px;color:var(--indigo)">$49.00</div>
    <div class="card-text" style="font-size:2.5px">Pay in 4 interest-free installments with Paylane.</div>
    <div style="margin-top:6px;border:1px solid #e0deea;height:8px;font-size:2.5px;padding:2px">13 / FEB / 2022</div>
    <div style="margin-top:5px;font-size:2.5px;color:var(--muted)">☐ Add Engraving</div>
    <div style="margin-top:2px;border:1px solid #e0deea;height:7px;font-size:2.5px;color:var(--muted);padding:1px 2px">Type Your Message Here</div>
    <div class="btn-solid" style="margin-top:24px;height:9px;font-size:2.5px">ADD TO CART</div>
  </div>
  <div class="abs" style="left:7px;top:955px;font-size:4px">Our Featured Products</div>
  <div class="photo ph-product" role="img" aria-label="Silver necklace with moon pendant" style="left:7px;top:970px;width:84px;height:81px"></div>
  <div class="abs" style="left:0;right:0;top:1054px;text-align:center;font-size:2.5px">Dawnline Necklace in Silver<br>$49</div>
  <div class="photo ph-product" role="img" aria-label="Gold chain necklace with blue pendant" style="left:7px;top:1077px;width:84px;height:81px"></div>
  <div class="abs" style="left:0;right:0;top:1161px;text-align:center;font-size:2.5px">Meridian Necklace in Gold<br>$60</div>
  <div class="photo ph-product" role="img" aria-label="Gold necklace with pendant" style="left:7px;top:1184px;width:84px;height:82px"></div>
  <div class="abs" style="left:0;right:0;top:1269px;text-align:center;font-size:2.5px">Harbor Necklace in Gold<br>$95</div>
  <div class="photo ph-people" role="img" aria-label="Customers sharing their moments" style="left:0;top:1303px;width:96px;height:169px">
    <div class="abs" style="left:0;right:0;top:14px;text-align:center;color:#fff;font-size:4px">Moments that Matter</div>
    <div class="abs" style="left:0;right:0;top:50px;text-align:center;color:var(--indigo);font-size:3px">Tidewren Moment #128,005</div>
    <div class="abs" style="left:12px;right:12px;top:60px;text-align:center;color:var(--indigo);font-size:2.5px">Lorem ipsum dolor sit amet, consectetur adipiscing elit sed doe eiusmod tempor.</div>
  </div>
  <div class="abs" style="left:7px;top:1505px;width:84px;height:122px;background:var(--mist);text-align:center">
    <div style="font-size:2.5px;color:var(--muted);margin-top:6px">CELEBRATING YOUR LIFE</div>
    <div style="font-size:4px">Moments that Matter</div>
    <div class="card-text" style="font-size:2.5px;padding:4px 8px">Tidewren helps people stay connected to the memories that have shaped their life and their true selves.</div>
    <div class="btn-outline" style="margin:6px auto 0;width:36px;height:12px;font-size:2px">WHAT MOMENT WILL<br>YOU REMEMBER?</div>
  </div>
  <div class="abs" style="left:7px;top:1642px;font-size:4px">Learn More About<br>The Phases Now</div>
  <div class="photo ph-blog" role="img" aria-label="Capricorn essentials artwork with script lettering" style="left:7px;top:1677px;width:84px;height:85px"><div class="blog-word" style="top:24px;font-size:6px">CAPRICORN</div></div>
  <div class="abs" style="left:7px;top:1765px;font-size:3px">The Capricorn Essentials</div>
  <div class="photo ph-blog" role="img" aria-label="Libra essentials artwork with script lettering" style="left:7px;top:1807px;width:84px;height:83px"><div class="blog-word" style="top:24px;font-size:6px">THE LIBRA</div></div>
  <div class="abs" style="left:7px;top:1893px;font-size:3px">The Libra Essentials</div>
  <div class="photo ph-blog" role="img" aria-label="Sagittarius essentials artwork with script lettering" style="left:7px;top:1935px;width:84px;height:84px"><div class="blog-word" style="top:20px;font-size:5.5px">THE<br>SAGITTARIUS</div></div>
  <div class="abs" style="left:7px;top:2022px;font-size:3px">The Saggitarius Essentials</div>
  <div class="abs" style="left:0;top:2073px;width:96px;height:92px;background:var(--indigo);color:#fff;text-align:center">
    <div style="font-size:4px;margin-top:20px">Sign up for 10% off<br>your first purchase*</div>
    <div style="margin:10px auto 0;width:84px;height:9px;background:#fff;display:flex"><span style="flex:1"></span><span style="width:26px;background:var(--lilac)"></span></div>
  </div>
  <div class="abs" style="left:0;top:2165px;width:96px;height:77px;background:var(--lilac);color:#fff;text-align:center">
    <div style="font-size:4px;margin-top:16px">Gifts for<br>various occasions</div>
    <div class="btn-solid" style="margin:10px auto 0;width:34px;height:8px;font-size:2.5px">SHOP GIFTS</div>
  </div>
  <div class="press-badge" style="left:7px;top:2262px;width:24px;height:6px"></div>
  <div class="press-badge" style="left:53px;top:2262px;width:34px;height:6px"></div>
  <div class="press-badge" style="left:12px;top:2280px;width:14px;height:6px"></div>
  <div class="press-badge" style="left:58px;top:2280px;width:24px;height:6px"></div>
  <footer class="footer" style="top:2309px;height:189px">
    <div class="foot-head" style="left:7px;top:12px;font-size:3px">HELP</div>
    <ul class="foot-list" style="left:7px;top:18px;font-size:2.5px;line-height:2.2"><li>FAQs</li><li>Contact Us</li><li>Rewards</li><li>Track Your Order</li><li>Reviews</li><li>My Account</li></ul>
    <div class="foot-head" style="left:62px;top:12px;font-size:3px">COMPANY</div>
    <ul class="foot-list" style="left:62px;top:18px;font-size:2.5px;line-height:2.2"><li>About Us</li><li>Blog</li><li>Careers</li><li>Tours</li><li>Wholesale</li><li>Partnerships</li></ul>
    <div class="foot-head" style="left:7px;top:65px;font-size:3px">SHOP</div>
    <ul class="foot-list" style="left:7px;top:71px;font-size:2.5px;line-height:2.2"><li>Find Your Moon</li><li>Necklaces</li><li>Bracelets</li><li>Rings</li><li>Gifts</li><li>Deals</li></ul>
    <div class="foot-head" style="left:62px;top:65px;font-size:3px">FIND US</div>
    <div class="abs social" style="left:62px;top:71px;gap:2px"><span style="width:3px;height:3px"></span><span style="width:3px;height:3px"></span><span style="width:3px;height:3px"></span><span style="width:3px;height:3px"></span></div>
    <div class="abs" style="left:7px;top:140px;font-size:2.5px;color:var(--muted)">Terms &amp; Conditions | Privacy Policy<br>Copyright © Tidewren, LLC.</div>
  </footer>
</main>

</body>
</html>
```